Creative Typography Posters

I am looking for designers that would be interested in long-term co-operation and this is your chance to express your interest and show what you can deliver.

The task:
Choose any 10 quotes from the list and create 10 unique and original posters as per the specification. For easier review, concatenate them into one larger picture - side by side.

Specification:
* 2:3 ratio (portrait) - 1280x1920 pixels per poster
* the poster must be readable even in low resolutions (e.g. 320x480px)
* no copyrighted content (photographs, illustrations, fonts)
* designs that will match the quote/idea visually will be preferred
* be diverse, make each design different and interesting in its own way

Quotes:
* In the beginning there was nothing. God said, 'Let there be light!' And there was light. There was still nothing, but you could see it a whole lot better. -Marla Pettivoss

* Life isn’t about waiting for the storm to pass. It’s about dancing in the rain.

* All I ask is a chance to prove that money can't make me happy.

* The big difference between sex for money and sex for free is that sex for money usually costs a lot less. -Corwin Haldsby

* If you understand what you're doing, you're not learning anything. -T.W.

* To win without risk is to triumph without glory. -Gaston Vireleau

* Love the ones you can. Touch the ones you can reach. Let the others go.

* I would never die for my beliefs because I might be wrong. -Osmund Kettleby

* Never be afraid to do something new. Remember, amateurs built the ark; professionals built the colossa.

* Live as you would have wished to live when you are dying.

* The only way of finding the limits of the possible is by going beyond them into the impossible. -Morris T. Quade

* Feeling resistance means you're moving forward.

* A bottle of wine contains more philosophy than all the books in the world. -Henri Dumolay

* Man prefers to believe what he prefers to be true. -Edwin Marlowe

* If at first you don't succeed, failure may be your style. -Rupert Vanley

* Choose a job you love and you will never have to work a day in your life. -Meng Tavo

* Statisticians do it with 95% confidence.

* Just because no one saw it doesn't mean it didn't happen.

* Life begins at the end of your comfort zone

* And then my sould saw you and it kind of went "Oh there you are. I've been looking for you."

* Sometimes, the people with the worst pasts can create the best futures.

* Women are like the NVK, they already know what you have been up to, they just wait for the right moment to confront you.

Examples:
http://img.plakowave.com/2011/08/letter/2.jpg

http://media2.vexplorin.com/files/2010/10/39/0/1090/10906352/f992956978fe1d58_Red_Ember_v2_by_SirPorcupo.jpg

http://cdn.quibblor.com/wp-content/uploads/2012/03/typographic-poster-1.jpg

http://glimmerfeld.com/wp-content/uploads/2012/03/Typographic-Poster1.jpg

http://glimmerfeld.com/wp-content/uploads/2012/03/Typographic-Poster.jpg

http://data.trovumcdn.com/images/9868837/a0_size_typography_poster_by_lanternmoth47_large.jpg

Now, make art happen!

```html
<!DOCTYPE html>
<html lang="en">
<head>
<meta charset="utf-8">
<title>A bottle of wine contains more philosophy</title>
<link rel="stylesheet" href="https://fonts.googleapis.com/css2?family=Roboto:wght@500;700&display=swap">
<style>
  :root {
    --bg-green: #1e6b37;
    --bg-edge: #123f21;
    --bottle: #0f2c18;
    --text-light: #e3e3e1;
    --text-accent: #5bd93a;
  }
  html, body {
    margin: 0;
    padding: 0;
    width: 801px;
    height: 1200px;
    overflow: hidden;
  }
  .poster {
    position: relative;
    width: 801px;
    height: 1200px;
    overflow: hidden;
    background: radial-gradient(ellipse at 45% 45%, var(--bg-green) 0%, #1a6131 55%, var(--bg-edge) 100%);
    font-family: "Roboto", Arial, sans-serif;
  }
  .bottle-area {
    position: absolute;
    left: 500px;
    top: 0;
    width: 301px;
    height: 1200px;
    background: var(--bottle);
  }
  .quote-line {
    position: absolute;
    margin: 0;
    line-height: 1;
    font-weight: 700;
    letter-spacing: -0.02em;
    color: var(--text-light);
    white-space: nowrap;
    text-align: right;
  }
  .accent { color: var(--text-accent); }
  .line-top { right: 214px; }
  .line-body { right: 309px; }
  .attribution {
    position: absolute;
    right: 309px;
    top: 1031px;
    margin: 0;
    font-size: 34px;
    line-height: 1;
    font-weight: 500;
    color: var(--text-light);
  }
</style>
</head>
<body>
  <main class="poster">
    <div class="bottle-area" role="img" aria-label="Dark wine bottle silhouette"></div>

    <blockquote class="quote" style="margin:0">
      <p class="quote-line line-top" style="top:168px;font-size:86px">a bottle</p>
      <p class="quote-line line-top" style="top:254px;font-size:86px">of wine</p>
      <p class="quote-line line-body" style="top:349px;font-size:75px">contains</p>
      <p class="quote-line line-body accent" style="top:422px;font-size:75px">more</p>
      <p class="quote-line line-body" style="top:500px;font-size:68px">philosophy</p>
      <p class="quote-line line-body" style="top:583px;font-size:92px">than</p>
      <p class="quote-line line-body" style="top:678px;font-size:92px"><span class="accent">all</span> the</p>
      <p class="quote-line line-body" style="top:768px;font-size:96px">books</p>
      <p class="quote-line line-body" style="top:858px;font-size:72px">in the</p>
      <p class="quote-line line-body accent" style="top:928px;font-size:100px">world.</p>
    </blockquote>
    <p class="attribution">-Henri Dumolay</p>
  </main>
</body>
</html>
```